Criação de Kit Layout de Posts para Redes Sociais (Facebook, Instagram e etc) para Esportes
" Ofereço serviços de personal trainer para alunos em academias, condomínios, parques, etc.; serviços de personal trainer on-line ao vivo; e serviços de consultoria para prescrição de treinos (sem o acompanhamento durante a execução em si dos treinos) "

```html
<!DOCTYPE html>
<html lang="pt-BR">
<head>
<meta charset="utf-8">
<title>Rafael Moreira Personal Trainer – Post</title>
<link href="https://fonts.googleapis.com/css2?family=Montserrat:ital,wght@0,700;0,800;0,900;1,700;1,800;1,900&display=swap" rel="stylesheet">
<style>
  :root {
    --green: #37e04b;
    --green-dark: #0f6b22;
    --ink: #141414;
    --wall: #2a2a2a;
    --wall-light: #5b5b58;
    --white: #ffffff;
    --bar: #e9ece9;
  }
  html, body {
    margin: 0;
    padding: 0;
    width: 1200px;
    height: 1200px;
    overflow: hidden;
    background: var(--ink);
  }
  .post {
    position: relative;
    width: 1200px;
    height: 1200px;
    overflow: hidden;
    font-family: "Montserrat", sans-serif;
    color: var(--white);
  }
  .photo-area {
    position: absolute;
    inset: 0;
    background:
      radial-gradient(ellipse 420px 620px at 840px 520px, #8a7566 0%, #5a4c44 35%, rgba(40,40,40,0) 75%),
      radial-gradient(ellipse 700px 600px at 300px 300px, var(--wall-light) 0%, var(--wall) 60%, var(--ink) 100%);
  }
  .graphics {
    position: absolute;
    inset: 0;
  }
  .brand-box {
    position: absolute;
    left: 53px;
    top: 48px;
    width: 523px;
    height: 204px;
    background: var(--white);
    box-sizing: border-box;
    text-align: center;
  }
  .brand-mark {
    position: absolute;
    left: 236px;
    top: 34px;
    width: 52px;
    height: 52px;
    background: var(--green);
  }
  .brand-name {
    position: absolute;
    left: 0;
    right: 0;
    top: 100px;
    margin: 0;
    font-size: 44px;
    font-weight: 700;
    color: var(--ink);
    letter-spacing: 1px;
    line-height: 1;
  }
  .brand-role {
    position: absolute;
    left: 0;
    right: 0;
    top: 152px;
    margin: 0;
    font-size: 26px;
    font-weight: 800;
    color: var(--green);
    letter-spacing: 3px;
    line-height: 1;
  }
  .headline {
    position: absolute;
    left: 48px;
    top: 368px;
    margin: 0;
    font-size: 86px;
    font-weight: 900;
    font-style: italic;
    line-height: 92px;
    letter-spacing: 1px;
    text-shadow: 0 4px 10px rgba(0,0,0,.5);
  }
  .claim {
    position: absolute;
    left: 48px;
    top: 752px;
    margin: 0;
    font-size: 54px;
    font-weight: 900;
    font-style: italic;
    line-height: 1;
    text-shadow: 0 3px 8px rgba(0,0,0,.5);
  }
  .subclaim {
    position: absolute;
    left: 48px;
    top: 820px;
    margin: 0;
    font-size: 37px;
    font-weight: 800;
    font-style: italic;
    line-height: 48px;
    color: var(--green);
  }
  .contact-bar {
    position: absolute;
    left: 12px;
    top: 979px;
    width: 552px;
    height: 72px;
    background: var(--bar);
    clip-path: polygon(0 0, 100% 0, 96% 100%, 0 100%);
    box-sizing: border-box;
    padding-left: 60px;
    display: flex;
    align-items: center;
    font-size: 34px;
    font-weight: 900;
    font-style: italic;
    color: var(--ink);
  }
  .contact-list {
    position: absolute;
    left: 36px;
    top: 1068px;
    margin: 0;
    padding: 0;
    list-style: none;
  }
  .contact-item {
    display: flex;
    align-items: center;
    height: 40px;
    font-size: 28px;
    font-weight: 700;
    color: var(--white);
  }
  .contact-icon {
    width: 26px;
    height: 26px;
    margin-right: 14px;
    flex: none;
  }
</style>
</head>
<body>
<main class="post">
  <div class="photo-area" role="img" aria-label="Fotografia de uma mulher em top esportivo cinza mostrando o abdômen definido, com as mãos na cintura, diante de uma parede de concreto escura"></div>

  <svg class="graphics" width="1200" height="1200" viewBox="0 0 1200 1200" aria-hidden="true">
    <!-- diagonal accent bands -->
    <polygon points="560,1200 700,1200 1200,640 1200,480" fill="var(--green)" opacity="0.85"/>
    <polygon points="760,1200 820,1200 1200,780 1200,710" fill="var(--green)" opacity="0.55"/>
    <polygon points="380,1200 440,1200 1000,560 960,560" fill="var(--green-dark)" opacity="0.55"/>
    <polygon points="0,720 0,1200 160,1200 0,900" fill="var(--green-dark)" opacity="0.35"/>
    <polygon points="0,560 0,640 240,330 200,330" fill="var(--green)" opacity="0.35"/>
    <!-- top dashed strip -->
    <rect x="600" y="0" width="600" height="40" fill="var(--ink)"/>
    <g fill="var(--green)">
      <polygon points="630,10 690,10 680,30 620,30"/>
      <polygon points="720,10 780,10 770,30 710,30"/>
      <polygon points="810,10 870,10 860,30 800,30"/>
      <polygon points="900,10 960,10 950,30 890,30"/>
      <polygon points="990,10 1050,10 1040,30 980,30"/>
      <polygon points="1080,10 1140,10 1130,30 1070,30"/>
    </g>
    <!-- bottom dashed strip -->
    <rect x="600" y="1160" width="600" height="40" fill="var(--ink)"/>
    <g fill="var(--green)">
      <polygon points="630,1170 690,1170 680,1190 620,1190"/>
      <polygon points="720,1170 780,1170 770,1190 710,1190"/>
      <polygon points="810,1170 870,1170 860,1190 800,1190"/>
      <polygon points="900,1170 960,1170 950,1190 890,1190"/>
      <polygon points="990,1170 1050,1170 1040,1190 980,1190"/>
      <polygon points="1080,1170 1140,1170 1130,1190 1070,1190"/>
    </g>
    <!-- side frame -->
    <rect x="1176" y="40" width="24" height="1120" fill="var(--ink)"/>
    <rect x="1184" y="60" width="8" height="200" fill="var(--green)"/>
    <rect x="0" y="0" width="14" height="1200" fill="var(--ink)"/>
  </svg>

  <header class="brand-box">
    <span class="brand-mark"></span>
    <p class="brand-name">RAFAEL MOREIRA</p>
    <p class="brand-role">PERSONAL TRAINER</p>
  </header>

  <h1 class="headline">QUANDO A<br>GENTE QUER<br>A GENTE FAZ</h1>

  <p class="claim">NÃO TENHA DÚVIDA!</p>
  <p class="subclaim">Com um personal<br>você nunca estara sozinho</p>

  <div class="contact-bar">ENTRE EM CONTATO</div>

  <ul class="contact-list">
    <li class="contact-item">
      <svg class="contact-icon" viewBox="0 0 24 24" aria-hidden="true"><circle cx="12" cy="12" r="10.5" fill="none" stroke="#fff" stroke-width="2"/><path d="M8.5 6.5l2 2.5-1.2 1.5c.8 1.8 2.2 3.2 4 4l1.5-1.2 2.5 2-1 1.8c-4.5 0-9-4.5-9-9z" fill="#fff"/></svg>
      11 98765-4321
    </li>
    <li class="contact-item">
      <svg class="contact-icon" viewBox="0 0 24 24" aria-hidden="true"><rect x="2" y="2" width="20" height="20" rx="5" fill="none" stroke="#fff" stroke-width="2.4"/></svg>
      @personal_rafaelmoreira
    </li>
    <li class="contact-item">
      <svg class="contact-icon" viewBox="0 0 24 24" aria-hidden="true"><rect x="1.5" y="4.5" width="21" height="15" fill="#fff"/><path d="M2 5.5l10 7 10-7" fill="none" stroke="#141414" stroke-width="1.8"/></svg>
      personal.rafael@exemplo.com
    </li>
  </ul>
</main>
</body>
</html>
```